Healthcare IT company looking for business card design

We develop IT systems for healthcare that significantly reduces cost and improves quality.

We want a business card design that is professional and clean, and using the colors in our logo.

Target Market(s)

Doctors and decision makers in the healthcare industry

Industry/Entity Type

Healthcare

Contact Information for Business Card

It should include
Name and title, address, telephone

Tobias Vrenholt, CEO
+46 712 418257
tobias@kelvaro.se

Font styles to use
Serif

Colors
0355a3
ed282f

Requirements
Must have
• Clean design
• Professional feel
Nice to have
• N/A
Should not have
• N/A

```html
<!DOCTYPE html>
<html lang="en">
<head>
<meta charset="utf-8">
<title>Kelvaro business card</title>
<link rel="stylesheet" href="https://fonts.googleapis.com/css2?family=Lora:wght@400;600;700&display=swap">
<style>
  :root {
    --backdrop: #e9e9ea;
    --brand-blue-deep: #05609a;
    --brand-blue-light: #0587b0;
    --ink-blue: #0d5b96;
    --coral: #ec6a6e;
    --paper: #ffffff;
  }
  * { box-sizing: border-box; margin: 0; padding: 0; }
  html, body {
    width: 1200px;
    height: 1200px;
    overflow: hidden;
    background: var(--backdrop);
  }
  .canvas {
    position: relative;
    width: 1200px;
    height: 1200px;
  }
  .card {
    position: absolute;
    top: 481px;
    width: 420px;
    height: 240px;
    overflow: hidden;
  }
  .card--front {
    left: 147px;
    background: linear-gradient(210deg, var(--brand-blue-light) 0%, var(--brand-blue-deep) 100%);
  }
  .card--back {
    left: 633px;
    background: var(--paper);
  }
  .wordmark {
    position: absolute;
    left: 74px;
    top: 62px;
    display: flex;
    align-items: center;
    gap: 10px;
    font-family: "Lora", serif;
    font-weight: 600;
    font-size: 46px;
    line-height: 1;
    color: var(--paper);
  }
  .wordmark__dot {
    width: 12px;
    height: 12px;
    border-radius: 50%;
    background: var(--coral);
    margin-top: -22px;
  }
  .corner-block {
    position: absolute;
    width: 100px;
    height: 100px;
    background: var(--coral);
  }
  .card--front .corner-block {
    right: 0;
    bottom: 0;
    border-top-left-radius: 6px;
  }
  .card--back .corner-block {
    left: 0;
    top: 0;
    border-bottom-right-radius: 6px;
  }
  .contact {
    position: absolute;
    left: 214px;
    top: 100px;
    width: 160px;
    font-family: "Lora", serif;
    color: var(--ink-blue);
  }
  .contact__name {
    font-weight: 700;
    font-size: 17px;
    line-height: 1.2;
    white-space: nowrap;
  }
  .contact__title {
    font-size: 13px;
    margin-top: 4px;
    letter-spacing: 0.02em;
  }
  .contact__rule {
    border: none;
    border-top: 2px solid var(--ink-blue);
    margin: 10px 0 10px;
    width: 161px;
  }
  .contact__line {
    font-size: 16px;
    line-height: 22px;
    white-space: nowrap;
  }
</style>
</head>
<body>
  <main class="canvas">
    <section class="card card--front" aria-label="Card front">
      <div class="wordmark">
        <span class="wordmark__name">Kelvaro</span>
        <span class="wordmark__dot" aria-hidden="true"></span>
      </div>
      <div class="corner-block" aria-hidden="true"></div>
    </section>

    <section class="card card--back" aria-label="Card back">
      <div class="corner-block" aria-hidden="true"></div>
      <div class="contact">
        <p class="contact__name">Tobias Vrenholt</p>
        <p class="contact__title">CEO</p>
        <hr class="contact__rule">
        <p class="contact__line">+46 712 418257</p>
        <p class="contact__line">tobias@kelvaro.se</p>
      </div>
    </section>
  </main>
</body>
</html>
```